Business Card Design Project

business cards to match the logo design reference 1970674
specific details to be provided asap - message to follow
hello - thank you for the logo design (reference 1970674) which we are very happy with. In terms of business cards you presented a couple of options ie blue front/white back and then the reverse. Can we start with the white front version but change the text details to black font?
Actual details are as follows;
Dorian Whitcombe
Managing Director
e dorianwhitcombe@velantra.com.au
t +61 2 7315 2946
m +61 422 517 639
Suite 307, Level 3, 82 Penhallow St
Sydney, NSW 2000, Australia
www.velantra.com.au

```html
<!DOCTYPE html>
<html lang="en">
<head>
<meta charset="utf-8">
<title>Velantra Business Card</title>
<link rel="stylesheet" href="https://fonts.googleapis.com/css2?family=Source+Sans+3:wght@400;600;700&display=swap">
<style>
  :root {
    --stage: #e9ebee;
    --blue-top: #3aa9df;
    --blue-bottom: #0e6db3;
    --brand-blue: #1a75bb;
    --brand-grey: #6d6e71;
    --text-black: #111111;
    --card-white: #ffffff;
    --shadow: rgba(0, 0, 0, 0.28);
  }
  * { margin: 0; padding: 0; box-sizing: border-box; }
  html, body {
    width: 1200px;
    height: 900px;
    overflow: hidden;
    background: var(--stage);
    font-family: "Source Sans 3", sans-serif;
  }
  .canvas {
    position: relative;
    width: 1200px;
    height: 900px;
  }
  .card {
    position: absolute;
    top: 302px;
    width: 513px;
    height: 295px;
    border-radius: 18px;
    box-shadow: 0 6px 16px var(--shadow);
    overflow: hidden;
  }
  .card--front {
    left: 73px;
    background: linear-gradient(180deg, var(--blue-top) 0%, var(--blue-bottom) 100%);
  }
  .card--back {
    left: 616px;
    background: var(--card-white);
  }
  .front-wordmark {
    position: absolute;
    right: 48px;
    bottom: 38px;
    color: #ffffff;
    font-weight: 600;
    font-size: 42px;
    line-height: 1;
    letter-spacing: 0.5px;
  }
  .back-brand {
    position: absolute;
    left: 34px;
    top: 190px;
    display: flex;
    align-items: center;
    gap: 12px;
  }
  .back-brand__dot {
    width: 54px;
    height: 54px;
    border-radius: 50%;
    background: var(--brand-blue);
  }
  .back-brand__name {
    color: var(--brand-grey);
    font-weight: 600;
    font-size: 40px;
    line-height: 1;
    letter-spacing: 0.5px;
  }
  .contact {
    position: absolute;
    left: 300px;
    top: 40px;
    width: 196px;
    color: var(--text-black);
    font-size: 12px;
    line-height: 18px;
  }
  .contact__name {
    font-weight: 700;
    font-size: 18px;
    line-height: 22px;
  }
  .contact__title {
    font-size: 13.5px;
    line-height: 20px;
    margin-bottom: 32px;
  }
  .contact__lines { list-style: none; margin-bottom: 36px; }
  .contact__label {
    display: inline-block;
    width: 14px;
  }
  .contact__address { font-style: normal; }
</style>
</head>
<body>
<main class="canvas">
  <section class="card card--front" aria-label="Card front">
    <div class="front-wordmark">Velantra</div>
  </section>

  <section class="card card--back" aria-label="Card back">
    <div class="back-brand">
      <span class="back-brand__dot"></span>
      <span class="back-brand__name">Velantra</span>
    </div>
    <div class="contact">
      <p class="contact__name">Dorian Whitcombe</p>
      <p class="contact__title">Managing Director</p>
      <ul class="contact__lines">
        <li><span class="contact__label">t</span>+61 2 7315 2946</li>
        <li><span class="contact__label">m</span>+61 422 517 639</li>
        <li><span class="contact__label">e</span>dorianwhitcombe@velantra.com.au</li>
      </ul>
      <address class="contact__address">
        Suite 307, Level 3, 82 Penhallow St<br>
        Sydney, NSW 2000, Australia<br>
        <span class="contact__web">www.velantra.com.au</span>
      </address>
    </div>
  </section>
</main>
</body>
</html>
```